Find Bright Harbor Business Card and logo

We need a logo design and business card for a new consulting firm called Find Bright Harbor. We specialize in Digital Transformation of enterprises of all sizes. We help enterprises understand & significantly increase their business velocity. This requires changes in culture, organization, process and technology. We also partner with advanced technology companies to deliver tangible accelerated solutions. Methods utilized include Agile, Design Thinking, Advanced Technology Platforms (microservices, digital data, virtualization, blockchain, etc.). The final design should communicate velocity, transformation, growth and innovation.

Target Market(s)

Large Corporations and Enterprises

Contact Information for Business Card

Tagline - Shape the Coming

Logo Text

Find Bright Harbor or an initial or initials or a symbol/picture

Requirements
Must have
• Front side: Logo, name of business (Find Bright Harbor), tagline (Shape the Coming)
• Back side: First Name, Last Name, Title, Mobile Phone, Email, LinkedIn, URL (findbrightharbor.com)
Nice to have
• The design should communicate velocity, transformation, growth and/or innovation.

```html
<!DOCTYPE html>
<html lang="en">
<head>
<meta charset="utf-8">
<title>Find Bright Harbor – Business Card</title>
<link rel="stylesheet" href="https://fonts.googleapis.com/css2?family=Lato:wght@400;700&family=Montserrat:wght@500;600&display=swap">
<style>
  :root {
    --bg: #141414;
    --card: #1f1f1f;
    --card-edge: #2a2a2a;
    --emboss: #2d2d2d;
    --emboss-light: #4a4a4a;
    --white: #f2f2f2;
    --blue: #1f6fb8;
    --muted: #d9d9d9;
  }
  * { margin: 0; padding: 0; box-sizing: border-box; }
  html, body { width: 1200px; height: 900px; overflow: hidden; }
  body {
    background: radial-gradient(ellipse at 60% 40%, #262626 0%, var(--bg) 70%);
    font-family: "Lato", sans-serif;
    position: relative;
  }
  .card {
    position: absolute;
    left: 250px;
    width: 700px;
    height: 400px;
    background: linear-gradient(135deg, #1c1c1c 0%, var(--card) 55%, #2a2a2a 100%);
    border: 1px solid var(--card-edge);
    box-shadow: 0 10px 30px rgba(0,0,0,0.6);
  }
  .card--front { top: 40px; }
  .card--back { top: 470px; }

  /* front */
  .front-lockup {
    position: absolute;
    inset: 0;
    display: flex;
    flex-direction: column;
    align-items: center;
    justify-content: center;
  }
  .front-name {
    font-family: "Lato", sans-serif;
    font-weight: 700;
    font-size: 40px;
    letter-spacing: 3px;
    text-transform: uppercase;
    color: var(--emboss);
    text-shadow: 1px 1px 0 var(--emboss-light), -1px -1px 0 #111;
  }
  .front-tagline {
    margin-top: 6px;
    font-size: 15px;
    letter-spacing: 6px;
    text-transform: uppercase;
    color: var(--emboss);
    text-shadow: 1px 1px 0 var(--emboss-light);
  }

  /* back */
  .back-brand {
    position: absolute;
    left: 50px;
    top: 150px;
    width: 330px;
  }
  .back-name {
    font-weight: 700;
    font-size: 27px;
    letter-spacing: 1.5px;
    text-transform: uppercase;
    color: var(--white);
  }
  .back-tagline {
    margin-top: 4px;
    font-size: 12px;
    letter-spacing: 5px;
    text-transform: uppercase;
    color: var(--white);
    text-align: right;
  }
  .divider {
    position: absolute;
    left: 420px;
    top: 110px;
    width: 2px;
    height: 190px;
    background: var(--blue);
  }
  .contact {
    position: absolute;
    left: 445px;
    top: 108px;
    color: var(--white);
  }
  .person-name {
    font-family: "Montserrat", sans-serif;
    font-weight: 600;
    font-size: 26px;
    letter-spacing: 1px;
    text-transform: uppercase;
    color: var(--blue);
  }
  .person-title { font-size: 17px; margin-bottom: 16px; }
  .address { font-size: 17px; line-height: 1.3; margin-bottom: 12px; }
  .contact-line {
    display: flex;
    align-items: center;
    gap: 8px;
    font-size: 17px;
    line-height: 1.4;
  }
  .contact-line svg { width: 12px; height: 12px; flex: none; }
</style>
</head>
<body>
  <section class="card card--front">
    <div class="front-lockup">
      <div class="front-name">Find Bright Harbor</div>
      <div class="front-tagline">Shape the Coming</div>
    </div>
  </section>

  <section class="card card--back">
    <div class="back-brand">
      <div class="back-name">Find Bright Harbor</div>
      <div class="back-tagline">Shape the Coming</div>
    </div>
    <div class="divider"></div>
    <div class="contact">
      <div class="person-name">Daniel Reyes</div>
      <div class="person-title">Director</div>
      <div class="address">27 Alder Lane<br>Westbrook, VA 22910</div>
      <div class="contact-line">
        <svg viewBox="0 0 12 12" aria-hidden="true"><path d="M2.5 1 L4.5 1 L5.2 3.5 L4 4.5 Q5 7 7.5 8 L8.5 6.8 L11 7.5 L11 9.5 Q10 11 8 10.5 Q2.5 8.5 1 3.5 Q1 1.8 2.5 1 Z" fill="var(--blue)"/></svg>
        <span>555 014-2290</span>
      </div>
      <div class="contact-line">
        <svg viewBox="0 0 12 12" aria-hidden="true"><rect x="1" y="2.5" width="10" height="7" fill="none" stroke="var(--blue)" stroke-width="1.2"/><path d="M1 2.5 L6 6.5 L11 2.5" fill="none" stroke="var(--blue)" stroke-width="1.2"/></svg>
        <span>info@findbrightharbor.com</span>
      </div>
      <div class="contact-line">
        <svg viewBox="0 0 12 12" aria-hidden="true"><circle cx="6" cy="6" r="5" fill="none" stroke="var(--blue)" stroke-width="1.1"/><ellipse cx="6" cy="6" rx="2.2" ry="5" fill="none" stroke="var(--blue)" stroke-width="1"/><path d="M1 6 H11" stroke="var(--blue)" stroke-width="1"/></svg>
        <span>www.findbrightharbor.com</span>
      </div>
    </div>
  </section>
</body>
</html>
```